Hadley & Partners, LLC Business Card 2016

We need a new business card design for a very important trade show coming up.

We are a compliance Consulting Firm. Our clients are stock brokerage firms and investment advisers.

I would like our logo on both sides of the card.

Info in the front of the card shold include:

Logo
First & Last Name
Title
Office #
Cell #
Email
Company Address (42 W. Calloway St., Suite 300 Pasadena, CA 91417

Back of the card should include the logo and url: www.hadleypartnersgroup.com

Target Market(s)

Stock Brokerage Firms and Investment Advisers

Industry/Entity Type

Financial Service

Contact Information for Business Card

Marcus J. Pellew
President
42 W. Calloway St., Suite 300
Pasadena, CA 91417
O 626.555.0147 ext. 204
C 818.555.0193
Email: marcus@hadleypartnersgroup.com
www.hadleypartnersgroup.com

Requirements
Nice to have
• The back of the card could be black with the logo with the white letters.
• I do want the front of the card to at least have the color logo with the black "Hadley & Partners Lettering.

```html
<!DOCTYPE html>
<html lang="en">
<head>
<meta charset="utf-8">
<title>Hadley &amp; Partners — Business Card</title>
<link rel="stylesheet" href="https://fonts.googleapis.com/css2?family=Cinzel:wght@400&family=Lato:wght@400;700&display=swap">
<style>
  :root {
    --backdrop: #4a3428;
    --card-black: #000000;
    --card-white: #ffffff;
    --brand-red: #c9302a;
    --stripe-red: #d2312b;
    --stripe-grey: #9a9ea3;
    --text-grey: #5f6266;
    --rule-grey: #d9dadc;
    --wordmark-white: #f4f4f4;
  }
  * { margin: 0; padding: 0; box-sizing: border-box; }
  html, body { width: 1200px; height: 1000px; overflow: hidden; }
  body { background: var(--backdrop); position: relative; font-family: "Lato", sans-serif; }

  .card { position: absolute; left: 243px; width: 708px; height: 405px; }
  .card--back { top: 84px; background: var(--card-black); display: flex; align-items: center; justify-content: center; }
  .card--front { top: 526px; background: var(--card-white); }

  .wordmark { font-family: "Cinzel", serif; font-weight: 400; color: var(--wordmark-white); text-align: center; line-height: 1; }
  .wordmark__main { display: block; font-size: 54px; letter-spacing: 1px; }
  .wordmark__sub { display: block; font-size: 27px; letter-spacing: 7px; margin-top: 4px; }

  .front-mark { position: absolute; left: 40px; top: 95px; width: 280px; height: 200px; display: flex; flex-direction: column; justify-content: center; align-items: center; }
  .front-mark .wordmark { color: var(--brand-red); }
  .front-mark .wordmark__main { font-size: 44px; }
  .front-mark .wordmark__sub { font-size: 22px; letter-spacing: 5px; }

  .divider { position: absolute; left: 335px; top: 114px; width: 1px; height: 182px; background: var(--rule-grey); }

  .contact { position: absolute; left: 361px; top: 106px; color: var(--text-grey); font-size: 16px; line-height: 22px; }
  .contact__name { color: var(--brand-red); font-weight: 700; font-size: 21px; line-height: 26px; }
  .contact__title { margin-bottom: 12px; }
  .contact__address { margin-bottom: 12px; }
  .contact__list { list-style: none; }
  .contact__list li { display: flex; align-items: center; gap: 6px; height: 22.5px; }
  .contact__list svg { width: 12px; height: 12px; flex: none; fill: var(--brand-red); }

  .stripe { position: absolute; left: 0; right: 0; }
  .stripe--red { top: 382px; height: 11px; background: var(--stripe-red); }
  .stripe--grey { top: 393px; height: 12px; background: var(--stripe-grey); }
  .stripe__name { position: absolute; right: 104px; top: 1px; font-family: "Cinzel", serif; font-size: 8px; color: var(--card-white); letter-spacing: 1px; line-height: 9px; }
</style>
</head>
<body>
  <section class="card card--back">
    <div class="wordmark">
      <span class="wordmark__main">HADLEY</span>
      <span class="wordmark__sub">&amp; PARTNERS</span>
    </div>
  </section>

  <section class="card card--front">
    <div class="front-mark">
      <div class="wordmark">
        <span class="wordmark__main">HADLEY</span>
        <span class="wordmark__sub">&amp; PARTNERS</span>
      </div>
    </div>

    <div class="divider"></div>

    <div class="contact">
      <p class="contact__name">Marcus J. Pellew</p>
      <p class="contact__title">President</p>
      <p class="contact__address">42 W. Calloway St., Suite 300<br>Pasadena, CA 91417</p>
      <ul class="contact__list">
        <li><svg viewBox="0 0 12 12" aria-hidden="true"><path d="M1 4.5C1 3 2.5 2 6 2s5 1 5 2.5v1H8.5V4.2h-5v1.3H1z"/><path d="M3 6.3h6l1.5 3.7h-9z"/></svg>626.555.0147 ext. 204</li>
        <li><svg viewBox="0 0 12 12" aria-hidden="true"><path d="M3.5 0.5h5a1 1 0 0 1 1 1v9a1 1 0 0 1-1 1h-5a1 1 0 0 1-1-1v-9a1 1 0 0 1 1-1zM4 2v7h4V2zm2 7.6a.6.6 0 1 0 0 1.2.6.6 0 0 0 0-1.2z"/></svg>818.555.0193</li>
        <li><svg viewBox="0 0 12 12" aria-hidden="true"><path d="M1 3h10v.6L6 7 1 3.6z"/><path d="M1 4.6l5 3.4 5-3.4V9.5H1z"/></svg>marcus@hadleypartnersgroup.com</li>
        <li><svg viewBox="0 0 12 12" aria-hidden="true"><path d="M6 1a5 5 0 1 0 0 10A5 5 0 0 0 6 1zm0 1c.7.6 1.2 1.7 1.4 3H4.6C4.8 3.7 5.3 2.6 6 2zM3.6 5H2.1a4 4 0 0 1 2.3-2.7C3.9 3 3.7 4 3.6 5zm0 1c.1 1 .3 2 .8 2.7A4 4 0 0 1 2.1 6zm1 0h2.8c-.2 1.3-.7 2.4-1.4 3-.7-.6-1.2-1.7-1.4-3zm3.8 0h1.5a4 4 0 0 1-2.3 2.7c.5-.7.7-1.7.8-2.7zm0-1c-.1-1-.3-2-.8-2.7A4 4 0 0 1 9.9 5z"/></svg>www.hadleypartnersgroup.com</li>
      </ul>
    </div>

    <div class="stripe stripe--red"><span class="stripe__name">HADLEY &amp; PARTNERS</span></div>
    <div class="stripe stripe--grey"></div>
  </section>
</body>
</html>
```